Flyer-Design
Sehr flexibel bei Änderungswünschen. Herzlichen Dank. Würde jederzeit wieder mit Ursula zusammenarbeiten.
Zielgruppe
Wir sind eine eine Praxis und unsere Zielgruppe sind Kunden. Es sollte einen Faltflyer geben, welcher Doppelseitig bedruckt wird.
Aufgabenstellung
Ich habe genaue Vorstellungen, wie dieser Flyer aussehen soll. Jedoch bin ich auch auf neue Ideen gespannt :). Wunschvorstellung wäre ein Falzflyer (siehe Bild Musterfyler). Des weiteren habe ich ein Word gemacht, mit dem gesamten Inhalt des Textes und wie der Flyer am Besten aufgebaut werden sollte. (siehe Flyer Tierversicherung).
Die beiden letzten Abschnitte (Tipp an unsere Kunden, Fazit) sollten ein wenig auffallen. Müssen auch nicht am Schluss sein.
Des weiteren wäre ich dankbar, wenn das CI/CD der Unternehmung berücksichtig wird. Bitte werfen Sie einen Blick auf die Webseite www.felbor-tieraerzte.ch. Ein Logo ist ebenfalls im Anhang. Bei Fragen bitte melden.
Ich freue mich auf Vorschläge.

```html
<!DOCTYPE html>
<html lang="de">
<head>
<meta charset="utf-8">
<title>Felbor Tierärzte – Falzflyer Tierversicherung</title>
<link rel="stylesheet" href="https://fonts.googleapis.com/css2?family=Nunito:wght@400;600;700;800&family=Karla:wght@400&display=swap">
<style>
:root{
  --brand:#d0104c;
  --ink:#222;
  --muted:#8d8d8d;
  --panel-grey:#f2f2f2;
  --page:#fff;
  --fur-grey:#8a8178;
  --fur-orange:#c8793a;
}
*{box-sizing:border-box;margin:0;padding:0}
html,body{width:849px;height:1200px;overflow:hidden;background:var(--page)}
body{position:relative;font-family:"Nunito",sans-serif;color:var(--ink)}
.sheet-title{position:absolute;left:36px;top:36px;font-family:"Karla",sans-serif;font-size:15px;letter-spacing:.6px}
.panel-label{position:absolute;top:110px;font-family:"Karla",sans-serif;font-size:11px;letter-spacing:.4px}
.section-label{position:absolute;left:36px;top:598px;font-family:"Karla",sans-serif;font-size:11px;letter-spacing:.4px}

.spread{position:absolute;left:36px;width:777px;height:410px;box-shadow:0 1px 4px rgba(0,0,0,.25);overflow:hidden;background:#fff}
.spread--outer{top:149px}
.spread--inner{top:638px}
.panel{position:absolute;top:0;width:194.25px;height:410px}
.panel--fold2{left:0;background:var(--panel-grey)}
.panel--back{left:194.25px}
.panel--cover{left:388.5px}
.panel--fold1{left:582.75px}

.bar{position:absolute;left:0;right:0;height:25px;background:var(--brand);color:#fff;display:flex;align-items:center;padding-left:17px}
.bar--top{top:0;font-size:5.8px;font-weight:700}
.bar--top strong{font-size:10px;font-weight:800;margin-left:2px}
.bar--bottom{top:385px;font-size:10px;font-weight:700;letter-spacing:1.4px}

.wordmark{position:absolute;left:17px;top:42px;color:var(--brand);font-weight:800;line-height:1}
.wordmark__name{display:block;font-size:19px;letter-spacing:1.5px;text-transform:uppercase}
.wordmark__sub{display:block;font-size:19px;letter-spacing:1.5px;text-transform:uppercase;margin-left:50px;margin-top:2px}

.intro{position:absolute;left:20px;top:26px;width:162px;font-size:6.3px;line-height:10.3px}
.intro p{margin-bottom:20px}
.intro__callout{color:var(--brand);font-weight:800;font-size:10px;line-height:13.8px;margin-top:-2px}

.hours{position:absolute;left:17px;top:116px;width:170px;font-size:8.4px;color:var(--muted);line-height:11.5px}
.hours__title{color:var(--brand);font-weight:700;font-size:9px;text-decoration:underline;text-underline-offset:2px;margin-bottom:6px}
.hours__row{display:flex;margin-bottom:12px}
.hours__day{width:50px}
.address{position:absolute;left:17px;top:262px;font-size:8.4px;line-height:11.6px;color:var(--muted)}
.address__name{color:var(--brand);font-weight:700}
.address__mail{color:var(--brand);font-weight:700;margin-top:11px}

.cover-band{position:absolute;left:0;top:101px;width:100%;height:128px;background:var(--panel-grey);padding:14px 0 0 18px;color:var(--brand)}
.cover-band h1{font-size:18.5px;font-weight:800;line-height:25px}
.cover-band__sub{font-size:12.5px;font-weight:800;margin-top:8px}
.photo{position:absolute;left:0;width:100%}
.photo--paws{top:229px;height:156px;background:linear-gradient(120deg,#e6e4e0 0%,#d9d6d0 40%,#e8c8a8 62%,#c77a3a 85%,#b86a2c 100%)}
.photo--fur-grey{top:0;height:24px;background:linear-gradient(90deg,#6f665d,#a79d92 30%,#5d554d 55%,#9c9288 80%,#746b61)}
.photo--fur-orange{top:385px;height:25px;background:linear-gradient(90deg,#c06d2c,#d48a48 50%,#b9652a 75%,#e9d6c6 92%,#c57a3c)}

.tip{position:absolute;left:0;top:24px;width:100%;height:205px;background:var(--brand);color:#fff;padding:13px 10px 0 18px}
.tip h2{font-size:20px;font-weight:800;line-height:25px}
.tip p{font-size:10px;line-height:13.9px;margin-top:8px;letter-spacing:.2px}
.fazit{position:absolute;left:18px;top:268px;width:168px}
.fazit h2{color:var(--brand);font-size:10.5px;font-weight:800;margin-bottom:11px}
.fazit p{font-size:6.3px;line-height:10.3px}

.column{position:absolute;top:26px;width:157px}
.column--1{left:20px}.column--2{left:211px}.column--3{left:408px}.column--4{left:600px}
.letter{color:var(--brand);font-weight:800;font-size:9px;border-bottom:.8px solid var(--brand);padding-bottom:1px;margin-bottom:8px}
.entry{margin-bottom:9px}
.entry h3{color:var(--brand);font-size:5.1px;font-weight:800;line-height:9px}
.entry p{font-size:5.1px;line-height:9.3px}
.letter-group{margin-bottom:20px}
.imprint{position:absolute;left:0;right:0;top:385px;height:25px;background:var(--brand);color:#fff;display:flex;align-items:center;justify-content:space-between;padding:0 19px 0 21px;font-size:8.6px;font-weight:700;letter-spacing:.9px}
</style>
</head>
<body>
<div class="sheet-title">Falzflyer/Faltblätter, Dreibruch-Fensterfalz, 8 Seiten</div>
<div class="panel-label" style="left:36px">Einklappseite 2</div>
<div class="panel-label" style="left:229px">Rückseite</div>
<div class="panel-label" style="left:423px">Titelseite</div>
<div class="panel-label" style="left:620px">Einklappseite 1</div>

<section class="spread spread--outer">
  <div class="panel panel--fold2">
    <div class="intro">
      <p>Haustiere sind für viele von uns von grosser Bedeutung und sensible Weggefährten, mit denen sich lachen, reden und auch einmal weinen lässt. Neben den vielen Vorzügen, die ein eigenes Haustier mit sich bringen, können diese auch krank werden oder einen Unfall haben.</p>
      <p>Wenn eine Behandlung das geliebte Haustier retten kann, jedoch hohe Kosten für Medikamente, Behandlungen, Operationen oder Klinikaufenthalte auslöst, dann entstehen bei vielen Personen ernsthafte Sorgen und Belastungen, denen allerdings vorgebeugt werden kann.</p>
      <p>Mit einem Abschluss einer Tierversicherung gegen Unfall und Krankheit können verschiedene Vorkehrungen getroffen werden, um hohe Kosten im Ernstfall zu reduzieren.</p>
      <p>Daher ist es wichtig, dass man sich vorgängig über die Möglichkeiten einer Tierversicherung gegen Unfall und Krankheit informiert, um bestmöglich vorbereitet zu sein, sollte es dem treuen Begleiter einmal schlecht gehen.</p>
      <p class="intro__callout">In diesem Flyer finden Sie alles von A-Z, was Sie über Tierversicherungen gegen Unfall und Krankheit wissen müssen.</p>
    </div>
  </div>

  <div class="panel panel--back">
    <div class="bar bar--top">Praxis- und Notfallnummer <strong>041 555 01 20</strong></div>
    <div class="wordmark"><span class="wordmark__name">Felbor</span><span class="wordmark__sub">Tierärzte</span></div>
    <div class="hours">
      <div class="hours__title">Praxisöffnungszeiten</div>
      <div class="hours__row"><span class="hours__day">Mo bis Fr</span><span>8.00 – 12.00 und<br>13.30 - 18.00 Uhr</span></div>
      <div class="hours__row"><span class="hours__day">Sa</span><span>8.00 – 12.00 Uhr</span></div>
      <div>Dringende Notfälle auch ausserhalb der Kliniköffnungszeiten.</div>
    </div>
    <div class="address">
      <div class="address__name">Felbor Tierärzte</div>
      <div>Kleintier AG / Grosstier AG</div>
      <div>Lindenweg 7</div>
      <div>6400 Seedorf</div>
      <div>T 041 555 01 20</div>
      <div>F 041 555 01 24</div>
      <div class="address__mail">info@felbor-tieraerzte.ch</div>
    </div>
    <div class="bar bar--bottom">www.felbor-tieraerzte.ch</div>
  </div>

  <div class="panel panel--cover">
    <div class="bar bar--top">Praxis- und Notfallnummer <strong>041 555 01 20</strong></div>
    <div class="wordmark"><span class="wordmark__name">Felbor</span><span class="wordmark__sub">Tierärzte</span></div>
    <div class="cover-band">
      <h1>Tierversicherung<br>gegen Unfall<br>und Krankheit.</h1>
      <div class="cover-band__sub">Fluch oder Segen?</div>
    </div>
    <div class="photo photo--paws" role="img" aria-label="Foto: Hundepfote liegt in zwei Menschenhänden auf hellem Holzboden"></div>
    <div class="bar bar--bottom">www.felbor-tieraerzte.ch</div>
  </div>

  <div class="panel panel--fold1">
    <div class="photo photo--fur-grey" role="img" aria-label="Foto: getigertes graues Katzenfell"></div>
    <div class="tip">
      <h2>Tipp an unsere Kunden</h2>
      <p>Wir empfehlen Ihnen die die Tierarztkosten der letzten Jahre zusammenzustellen und zu prüfen, ob sie von der gewählten Versicherung übernommen worden wären. Bei diesem Vergleich darf aber der Selbstbehalt nicht ausser Acht gelassen werden.</p>
    </div>
    <div class="fazit">
      <h2>Fazit</h2>
      <p>Wir von der Felbor Tierärzte AG haben bisher sehr gute Erfahrungen mit Tierversicherungen unserer Kunden gemacht. Wir empfehlen Ihnen jedoch etwas Zeit in die Auswahl einer für sie passenden Tierversicherung zu investieren.</p>
    </div>
    <div class="photo photo--fur-orange" role="img" aria-label="Foto: orange-weisses Hundefell"></div>
  </div>
</section>

<div class="section-label">Innenseiten</div>

<section class="spread spread--inner">
  <div class="column column--1">
    <div class="letter">A</div>
    <div class="entry"><h3>Abschluss</h3><p>Beim Abschluss einer Versicherung muss das Tier jung und gesund sein.</p></div>
    <div class="entry"><h3>Anbieter</h3><p>Auf dem Schweizer Markt gibt verschiedene Anbieter von Tierversicherungen wie beispielsweise Tierwohl, Pfotenschutz, Fellfreund, Hausgard, Alvena und Genorma.</p></div>
    <div class="entry"><p>Wir empfehlen keinen konkreten Anbieter, da es viele verschiedene unterschiedliche Produkte auf dem Markt gibt und jeder Kunde andere Wünsche und ein anderes Budget hat. Unseres Erachtens liegen die Unterschiede im Detail.</p></div>
    <div class="entry"><h3>Altersbegrenzung</h3><p>Die Anbieter von Tierversicherungen haben Altersbegrenzungen, üblicherweise betragen diese fünf Jahre bei Katzen und sechs Jahre bei Hunden.</p></div>
    <div class="entry"><h3>Arztwahl</h3><p>Gewisse Versicherungen erlauben keine freie Tierarztwahl. Sichern Sie sich bei Vertragsabschluss ab und fragen, sie explizit nach.</p></div>
    <div class="entry"><h3>Aufnahmealter</h3><p>Die Versicherungsanbieter nehmen die Tiere in der Regel im Alter von 3 Monaten auf. Wir empfehlen die Tiere so früh wie möglich zu versichern.</p></div>
    <div class="entry"><h3>Ausschlüsse</h3><p>Beachten sie, ob Ausschlüsse aus einer Versicherungsleistung existieren und ob diese für sie von Bedeutung sind.</p></div>
  </div>

  <div class="column column--2">
    <div class="letter-group">
      <div class="letter">G</div>
      <div class="entry"><h3>Geburtskrankheiten/Erbkrankheiten</h3><p>Diese werden bei vielen Angeboten ausgeschlossen oder müssen explizit dazu versichert werden.</p></div>
    </div>
    <div class="letter-group">
      <div class="letter">I</div>
      <div class="entry"><h3>Impfungen</h3><p>Nur wenige Anbieter übernehmen auch Impfungen. Falls ein Anbieter diese Leistung übernimmt, hat er in der Regel einen maximalen Betrag festgelegt.</p></div>
    </div>
    <div class="letter-group">
      <div class="letter">K</div>
      <div class="entry"><h3>Karenzfrist</h3><p>Bei Versicherungen besteht jeweils eine Wartezeit, die zwischen Unterzeichnung der Police und einem Deckungsanspruch eingehalten werden muss. In der Regel beträgt diese für nicht-chronische Krankheiten einen Monat und bei chronischen Krankheiten drei Monate. Bei einem Unfall gibt es in der Regel keine Karenzfrist oder je nach Anbieter bis zu einem Monat.</p></div>
    </div>
    <div class="letter-group">
      <div class="letter">L</div>
      <div class="entry"><h3>Leistungen</h3><p>Die inkludierten Leistungen und die gebotene Abdeckung ist genau zu prüfen. Übernimmt der Versicherungsanbieter alle Behandlungen oder sind zum Beispiel chronische Krankheiten oder Erbkrankheiten ausgeschlossen. Ein Blick auf das Kleingedruckte beim Versicherungsangebot lohnt sich. Sie können ihr Tier entweder gegen Krankheit oder gegen Unfall oder gegen beides versichern, letzteres empfehlen wir Ihnen.</p></div>
    </div>
  </div>

  <div class="column column--3">
    <div class="letter-group">
      <div class="letter">P</div>
      <div class="entry"><h3>Prämien</h3><p>Die Prämien der einzelnen Anbieter fallen unterschiedlich aus, deshalb ist es wichtig Versicherungsangebote zu vergleichen, um den passenden Tarif für ihr Haustier zu finden.</p></div>
      <div class="entry"><h3>Prämienerhöhung</h3><p>Es gibt Versicherungen, die während der Laufzeit die Prämien erhöhen, andere bieten einen Pauschalbetrag an, damit Planungssicherheit geboten wird.</p></div>
      <div class="entry"><h3>Preis</h3><p>Langfristig ist billigste Vertragsoption oft nicht die beste, da einige Versicherungen mit einem günstigeren Preis starten und im Laufe der Jahre, wenn das Tier älter wird, den Tarif erhöht.</p></div>
    </div>
    <div class="letter-group">
      <div class="letter">R</div>
      <div class="entry"><h3>Rabatte</h3><p>Vereinzelte Versicherungsanbieter gewähren Rabatte, wenn in einem Versicherungsjahr keine Leistungen bezogen wurden.</p></div>
      <div class="entry"><h3>Rechnungsstellung</h3><p>Die erbrachten Leistungen durch den Tierarzt sind direkt vom Tierhalter zu bezahlen. Anschliessend kann die Rechnung beim Versicherungsanbieter eingereicht werden.</p></div>
    </div>
  </div>

  <div class="column column--4">
    <div class="letter-group">
      <div class="letter">S</div>
      <div class="entry"><h3>Schadenfall</h3><p>Wenn ein Schadensfall eintritt, direkt den Tierarzt aufsuchen und erst anschliessend den Fall bei der Versicherung melden und gleich die Kostenübernahme abklären. Die Rechnungskopie wird bei Behandlungsabschluss der Versicherung zu Prüfung und Begleichung weitergeleitet.</p></div>
      <div class="entry"><h3>Selbstbehalt</h3><p>Der Selbstbehalt gibt an, welche Kosten bei einem Versicherungsfall selbst zu tragen sind. Einige Anbieter bieten ebenfalls die Option mit CHF 0 an. Falls man bei der Prämie etwas sparen möchte, sollte der Selbstbehalt auf einen höheren Betrag festgelegt werden. Einige Versicherungsanbieter ziehen den Selbstbehalt bei jedem Krankheitsfall an und andere jährlich.</p></div>
    </div>
    <div class="letter-group">
      <div class="letter">V</div>
      <div class="entry"><h3>Versicherungsende</h3><p>Das Haustier ist solange versichert, wie der Halter die Prämien bezahlt und das Tier lebt.</p></div>
      <div class="entry"><h3>Versicherungssumme</h3><p>Dies ist der Höchstbetrag, den der Kunden von einem Versicherungsanbieter für eine Behandlung eines Haustieres erhält.</p></div>
      <div class="entry"><h3>Vertragsdauer</h3><p>Die Mindestlaufzeit von Tierversicherungen beträgt in der Regel ein Jahr.</p></div>
    </div>
  </div>

  <div class="imprint">
    <span>Felbor Tierärzte</span><span>Kleintier AG / Grosstier AG</span><span>Lindenweg 7</span><span>6400 Seedorf</span><span>T 041 555 01 20</span><span>F 041 555 01 24</span><span>info@felbor-tieraerzte.ch</span>
  </div>
</section>
</body>
</html>
```